Flyer required for podiatry clinic

DL Size please.
Wanting a design for a mail box flyer for the local area. Wanting to increase our customer base. The information on the attached word document needs to be included.
If stock photos are able to be fit in that would be appreciated
We cater from young children to the elderly so should be suitable for all.

Colors

Designer to choose colors to be used in the design.

```html
<!DOCTYPE html>
<html lang="en">
<head>
<meta charset="utf-8">
<title>Stepwell Podiatry – DL Flyer</title>
<link rel="stylesheet" href="https://fonts.googleapis.com/css2?family=Open+Sans:ital,wght@0,400;0,600;0,700;1,700&family=Comic+Neue:wght@700&family=Fredoka:wght@600&family=Nunito:wght@800&family=Varela+Round&family=PT+Sans:wght@400;700&display=swap">
<style>
:root{
  --bg:#808080;
  --paper:#f7f7f7;
  --blue:#3794bf;
  --navy:#1f5f86;
  --green:#94c03c;
  --green-dark:#5f8f1d;
  --footer:#8a93ab;
  --ink:#111;
  --heart:#f08a9a;
}
*{margin:0;padding:0;box-sizing:border-box}
html,body{width:1200px;height:1200px;overflow:hidden;background:var(--bg)}
.flyer{position:absolute;top:40px;width:527px;height:1120px;background:var(--paper);box-shadow:0 0 14px rgba(0,0,0,.35);overflow:hidden;font-family:'Open Sans',sans-serif}
.flyer--services{left:56px}
.flyer--offer{left:617px}
.brand{position:absolute;left:0;right:0;text-align:center;font-family:'Fredoka',sans-serif;font-weight:600;color:var(--blue);line-height:.92;letter-spacing:-1px}
.flyer--services .brand{top:52px;font-size:56px}
.flyer--offer .brand{top:62px;font-size:54px}
.photo{position:absolute}
.photo--hero{left:0;top:163px;width:527px;height:267px;background:linear-gradient(120deg,#d9e2f0 0%,#eef1f6 45%,#e8d4c8 60%,#3a5f9a 100%)}
.rule-green{position:absolute;left:0;top:430px;width:527px;height:8px;background:var(--green)}
.services{position:absolute;left:0;top:438px;width:527px;height:346px;background:var(--blue)}
.service-list{position:absolute;left:30px;top:28px;width:300px;list-style:none;font-family:'Nunito',sans-serif;font-weight:800;font-size:16.5px;color:#fff;letter-spacing:.8px;line-height:21px}
.service-list li{position:relative;padding-left:22px;margin-bottom:8px}
.service-list li::before{content:"♥";position:absolute;left:0;top:0;color:var(--heart);font-size:13px}
.photo--small{border:3px solid #fff}
.photo--hands{left:336px;top:60px;width:160px;height:110px;background:linear-gradient(135deg,#f1d8cc,#e4b9a6)}
.photo--heel{left:364px;top:104px;width:132px;height:168px;background:linear-gradient(180deg,#e3d7d0,#d49a88 70%,#efe6d6)}
.billing{position:absolute;left:29px;top:800px;width:470px;font-family:'Varela Round',sans-serif;font-size:17.5px;color:var(--navy);letter-spacing:1px;line-height:21px}
.locations{position:absolute;left:34px;top:858px;font-family:'Varela Round',sans-serif;color:#111}
.locations h3{font-weight:400;font-size:12px;color:var(--navy);margin-bottom:6px;letter-spacing:.5px}
.locations h3 span{color:var(--heart)}
.locations p{font-size:11.5px;margin-bottom:7px;white-space:nowrap}
.locations p::before{content:"✓ ";font-size:8px}
.locations small{font-size:8px}
.team{position:absolute;left:30px;top:953px;font-family:'PT Sans',sans-serif;font-size:12.5px;font-weight:700;color:#222}
.team strong{font-size:18px;color:var(--blue)}
.garden{position:absolute;left:0;top:985px;width:527px;height:58px;background:linear-gradient(180deg,rgba(247,207,60,0),rgba(247,207,60,.35) 40%,rgba(120,170,60,.25))}
.grass{position:absolute;left:0;top:1032px;width:527px;height:20px}
.footer{position:absolute;left:0;top:1048px;width:527px;height:72px;background:var(--footer);color:#fff;text-align:center}
.footer__web{font-family:'Open Sans',sans-serif;font-weight:700;font-size:19.5px;letter-spacing:1.5px;line-height:72px}
.offer-title{position:absolute;left:0;right:0;top:204px;text-align:center;font-family:'Comic Neue',sans-serif;font-weight:700;font-size:38px;color:var(--blue);letter-spacing:1px}
.offer-intro{position:absolute;left:40px;right:40px;top:252px;text-align:center;font-size:16.5px;font-weight:600;letter-spacing:.5px;line-height:22.5px;color:var(--ink)}
.offer-card{position:absolute;top:342px;width:219px;height:230px;background:var(--green);border-radius:8px;text-align:center}
.offer-card--one{left:31px}
.offer-card--two{left:275px}
.offer-card__label{margin-top:20px;font-family:'Comic Neue',sans-serif;font-weight:700;font-size:24px;color:#fff;text-decoration:underline;text-underline-offset:4px}
.offer-card__value{margin-top:0;font-family:'Fredoka',sans-serif;font-weight:600;font-size:78px;line-height:90px;color:var(--blue);letter-spacing:-2px}
.offer-card__value--dark{color:var(--navy)}
.offer-card__text{font-family:'PT Sans',sans-serif;font-size:16.5px;line-height:21px;color:#222;margin-top:6px}
.worried{position:absolute;left:0;right:0;top:592px;text-align:center;font-family:'PT Sans',sans-serif}
.worried h2{font-size:31px;font-weight:700;color:var(--blue);line-height:36px}
.worried p{font-size:18.5px;color:var(--green-dark);margin-top:2px}
.worried p.book{margin-top:11px}
.worried .heart{color:var(--heart);font-size:15px;margin:0 10px}
.deadline{position:absolute;left:30px;right:30px;top:718px;text-align:center;font-family:'Open Sans',sans-serif;font-style:italic;font-weight:700;font-size:24px;line-height:31px;color:var(--ink);letter-spacing:-.3px}
.limited{position:absolute;left:0;right:0;top:878px;text-align:center;font-family:'Comic Neue',sans-serif;font-weight:700;font-size:30px;color:var(--blue);letter-spacing:1px}
.footer__phone{display:block;padding-top:16px;font-family:'Open Sans',sans-serif;font-weight:700;font-size:24px;line-height:28px}
.footer__small{display:block;font-size:11px;font-weight:700}
</style>
</head>
<body>

<section class="flyer flyer--services">
  <div class="brand">Stepwell<br>Podiatry</div>
  <div class="photo photo--hero" role="img" aria-label="Photo of a podiatrist in blue gloves examining a patient's bare foot"></div>
  <div class="rule-green"></div>
  <div class="services">
    <ul class="service-list">
      <li>Heel Pain- Spurs and Plantar Fasciitis</li>
      <li>Orthotics</li>
      <li>Fungal Nail Infections (Laser treatment)</li>
      <li>Diabetes Foot Assessments</li>
      <li>Foot and ankle pain</li>
      <li>Flat Feet- Both adults and children</li>
      <li>Ingrown nails</li>
      <li>Corns/Callus</li>
    </ul>
    <div class="photo photo--small photo--hands" role="img" aria-label="Photo of hands massaging the sole of a foot"></div>
    <div class="photo photo--small photo--heel" role="img" aria-label="Photo of a heel and ankle resting on an orthotic insole"></div>
  </div>
  <p class="billing">BULK BILLING for GP EPC/ Care plans , DVA Card Holders.ClaimPoint and EFTPOS available</p>
  <div class="locations">
    <h3><span>♥</span> 3 Handy locations</h3>
    <p>Bramble Medical Centre: <small>Level 1, 18 Orchard Road Kelby Ph: 9100 2210</small></p>
    <p>Bramble Rehabilitation: <small>42 Linden Street Kelby Ph: 9100 4432</small></p>
    <p>Family Health Hub: <small>57 Orchard Road Kelby Ph: 9100 7788</small></p>
  </div>
  <p class="team"><strong>Podiatrist:</strong> Daniel Ashworth, Marla Quinton, Helen Corby</p>
  <div class="garden" role="img" aria-label="Illustrated row of yellow flowers"></div>
  <svg class="grass" viewBox="0 0 527 20" preserveAspectRatio="none" aria-hidden="true"><path d="M0 8 Q13 2 26 8 T52 8 T78 8 T104 8 T130 8 T156 8 T182 8 T208 8 T234 8 T260 8 T286 8 T312 8 T338 8 T364 8 T390 8 T416 8 T442 8 T468 8 T494 8 T527 8 V20 H0Z" fill="#94c03c"/></svg>
  <div class="footer"><span class="footer__web">www.stepwell-podiatry.com.au</span></div>
</section>

<section class="flyer flyer--offer">
  <div class="brand">Stepwell<br>Podiatry</div>
  <h1 class="offer-title">SPECIAL OFFER!</h1>
  <p class="offer-intro">We are offering a special price to celebrate the opening of our new location at the Family Health Hub.</p>
  <div class="offer-card offer-card--one">
    <div class="offer-card__label">OFFER 1</div>
    <div class="offer-card__value offer-card__value--dark">$40</div>
    <div class="offer-card__text">Initial appointments.<br>Full assessment and<br>treatment.</div>
  </div>
  <div class="offer-card offer-card--two">
    <div class="offer-card__label">OFFER 2</div>
    <div class="offer-card__value">FREE</div>
    <div class="offer-card__text">BIOMECHECNICAL<br>ASSESSMENT</div>
  </div>
  <div class="worried">
    <h2>Worried</h2>
    <p>about your or your Children’s flat feet or painful feet?</p>
    <p class="book"><span class="heart">♥</span>Book in now for an obligation free assessment.<span class="heart">♥</span></p>
  </div>
  <p class="deadline">To take advantage of these offers you need to call and make the appointment before 31st December 2018.</p>
  <p class="limited">*LIMITED SPOTS AVAILABLE</p>
  <div class="garden" role="img" aria-label="Illustrated row of yellow flowers"></div>
  <svg class="grass" viewBox="0 0 527 20" preserveAspectRatio="none" aria-hidden="true"><path d="M0 8 Q13 2 26 8 T52 8 T78 8 T104 8 T130 8 T156 8 T182 8 T208 8 T234 8 T260 8 T286 8 T312 8 T338 8 T364 8 T390 8 T416 8 T442 8 T468 8 T494 8 T527 8 V20 H0Z" fill="#94c03c"/></svg>
  <div class="footer">
    <span class="footer__phone">9100 7788</span>
    <span class="footer__small">www.stepwell-podiatry.com.au</span>
  </div>
</section>

</body>
</html>
```